Business Card Design For Marketing Agnecy LVT

Need business card design for marketing agency.

Dorian Pell
President, CEO
1-555-304-2917
dorian@lumenvaletrewards.net
www.LumenValeTrewards.biz

Back Side:
Boost Sales Using Rewards, Incentives & Giveaways
Get A Free Sample Package

Target Market(s)

B2B

Industry/Entity Type

Marketing

Contact Information for Business Card

Dorian Pell
President, CEO
1-555-304-2917

Back Side:
Get A Free Sample Package

Please note that my current url is OLD DESIGN. I am working on new design and want the business card to match color themes at least on new site. Here is the demo link for new site so you can see the colors I use, etc.

http://pagekilnstudio.example/qx/dorian/lvt_final/index.html

Requirements
Must have
• Please note that my current url is OLD DESIGN. I am working on new design and want the business card to match color themes at least on new site. Here is the demo link for new site so you can see the colors I use, etc.

Nice to have

Should not have

```html
<!DOCTYPE html>
<html lang="en">
<head>
<meta charset="utf-8">
<title>Lumen Vale Trewards – Business Card</title>
<link rel="stylesheet" href="https://fonts.googleapis.com/css2?family=Lato:wght@400;700;900&display=swap">
<style>
  :root {
    --backdrop: #d4d4cf;
    --brand-blue: #1877c2;
    --ink-grey: #4a4a4c;
    --card-white: #ffffff;
    --text-dark: #3b3b3d;
  }
  * { box-sizing: border-box; margin: 0; padding: 0; }
  html, body {
    width: 1200px; height: 801px; overflow: hidden;
    background: var(--backdrop);
    font-family: "Lato", Arial, sans-serif;
  }
  .stage {
    position: relative; width: 1200px; height: 801px;
    display: flex; align-items: center; justify-content: center; gap: 50px;
  }
  .card {
    position: relative; width: 530px; height: 303px;
    box-shadow: 0 10px 24px rgba(0,0,0,0.18);
    overflow: hidden;
  }
  .wordmark {
    position: absolute; left: 36px; top: 40px;
    display: flex; align-items: center; gap: 14px;
    white-space: nowrap;
  }
  .wordmark-dot {
    width: 24px; height: 24px; border-radius: 50%; flex: none;
  }
  .wordmark-name {
    font-weight: 900; font-size: 29px; letter-spacing: 1px;
    text-transform: uppercase; line-height: 1;
  }
  .wordmark-rule {
    position: absolute; left: 74px; right: 36px; top: 84px; height: 2px;
  }

  /* front */
  .card-front { background: var(--card-white); border-bottom: 4px solid var(--brand-blue); }
  .card-front .wordmark-dot,
  .card-front .wordmark-rule { background: var(--brand-blue); }
  .card-front .wordmark-name { color: var(--brand-blue); }
  .contact { position: absolute; left: 240px; top: 112px; }
  .contact-name { font-weight: 900; font-size: 24px; color: var(--brand-blue); line-height: 1.2; }
  .contact-title { font-size: 14px; color: var(--text-dark); margin: 2px 0 14px; }
  .contact-line {
    display: flex; align-items: center; gap: 10px;
    font-size: 12.5px; color: var(--text-dark); line-height: 22px;
  }
  .contact-line svg { width: 14px; height: 14px; flex: none; }

  /* back */
  .card-back { background: var(--brand-blue); color: #fff; }
  .card-back .wordmark-dot,
  .card-back .wordmark-rule { background: #fff; }
  .card-back .wordmark-name { color: #fff; }
  .tagline {
    position: absolute; left: 74px; top: 100px;
    font-size: 15px; letter-spacing: 1px; text-transform: uppercase; line-height: 1.4;
  }
  .offer { position: absolute; left: 74px; top: 160px; text-transform: uppercase; }
  .offer-lead { font-weight: 700; font-size: 14px; letter-spacing: 0.5px; line-height: 1.2; }
  .offer-free { font-weight: 700; font-size: 36px; color: var(--ink-grey); line-height: 1.05; letter-spacing: 2px; }
  .offer-item { font-weight: 700; font-size: 14px; letter-spacing: 0.5px; line-height: 1.2; }
  .back-url {
    position: absolute; right: 30px; bottom: 24px;
    font-size: 16px; letter-spacing: 1.5px;
  }
</style>
</head>
<body>
<main class="stage">
  <section class="card card-front" aria-label="Card front">
    <div class="wordmark">
      <span class="wordmark-dot"></span>
      <span class="wordmark-name">Lumen Vale Trewards</span>
    </div>
    <div class="wordmark-rule"></div>
    <div class="contact">
      <p class="contact-name">Dorian Pell</p>
      <p class="contact-title">President &amp; CEO</p>
      <p class="contact-line">
        <svg viewBox="0 0 16 16"><path d="M4 1l3 3-2 2c1 2 3 4 5 5l2-2 3 3-2 3C7 15 1 9 1 3z" fill="#1877c2"/></svg>
        1-555-304-2917
      </p>
      <p class="contact-line">
        <svg viewBox="0 0 16 16"><rect x="1" y="3" width="14" height="10" fill="#1877c2"/><path d="M1 3l7 6 7-6" fill="none" stroke="#fff" stroke-width="1.4"/></svg>
        dorian@lumenvaletrewards.net
      </p>
      <p class="contact-line">
        <svg viewBox="0 0 16 16"><circle cx="8" cy="8" r="7" fill="none" stroke="#1877c2" stroke-width="1.6"/><path d="M1 8h14M8 1c3 3 3 11 0 14M8 1c-3 3-3 11 0 14" fill="none" stroke="#1877c2" stroke-width="1.2"/></svg>
        www.LumenValeTrewards.biz
      </p>
    </div>
  </section>

  <section class="card card-back" aria-label="Card back">
    <div class="wordmark">
      <span class="wordmark-dot"></span>
      <span class="wordmark-name">Lumen Vale Trewards</span>
    </div>
    <div class="wordmark-rule"></div>
    <p class="tagline">Boost sales using rewards,<br>incentives &amp; giveaways</p>
    <div class="offer">
      <p class="offer-lead">Get a</p>
      <p class="offer-free">Free</p>
      <p class="offer-item">Sample package</p>
    </div>
    <p class="back-url">www.LumenValeTrewards.biz</p>
  </section>
</main>
</body>
</html>
```